Hollow Lantern Distillery

I need a label designed for my small distillery. I’d like it to have a rose, and the name hollow lantern in script writing. I need the graphic to fit a standard gin bottle and I’ll need to be able to edit it depending on alcohol, warning and descriptions. I want it to look elegant and attractive, but slightly daring too. It’s a 700ml oslo bottle
Target Market(s)
Bespoke gin and vodka drinkers
Industry/Entity Type
Beverage
Font styles to use
Script
Other font styles liked:
- Something easy to read
Requirements
Must have
- Room for me to add and remove text depending on the drink
Nice to have
- Hollow lantern in script, slight colour on the rose and black writing

```html
<!DOCTYPE html>
<html lang="en">
<head>
<meta charset="utf-8">
<title>Hollow Lantern Distillery — Gin Label</title>
<link rel="stylesheet" href="https://fonts.googleapis.com/css2?family=Pinyon+Script&family=Mrs+Saint+Delafield&family=Montserrat:wght@600&family=Oswald:wght@500;600&display=swap">
<style>
  :root {
    --page: #f3f3f2;
    --label-light: #ebece8;
    --label-mid: #d8dad4;
    --info-band: #e6e7ea;
    --ink: #141414;
    --rule: #4a4a4a;
    --gold: #d9b45a;
    --rose: #f0b9bc;
    --rose-deep: #e58f98;
    --leaf: #6f9a6a;
  }
  * { box-sizing: border-box; margin: 0; padding: 0; }
  html, body {
    width: 960px; height: 1200px; overflow: hidden;
    background: var(--page);
  }
  .canvas { position: relative; width: 960px; height: 1200px; }
  .label {
    position: absolute; left: 180px; top: 75px;
    width: 600px; height: 1050px; overflow: hidden;
    background: linear-gradient(100deg, var(--label-light) 0%, var(--label-mid) 55%, var(--label-light) 100%);
  }
  .art { position: absolute; }
  .art--rose-top {
    left: 0; top: 0; width: 420px; height: 280px;
    background: radial-gradient(ellipse at 38% 42%, var(--rose-deep) 0%, var(--rose) 40%, rgba(240,185,188,0) 72%);
  }
  .art--leaves {
    left: 0; top: 250px; width: 95px; height: 270px;
    background: radial-gradient(ellipse at 20% 50%, var(--leaf) 0%, rgba(111,154,106,0.4) 50%, rgba(111,154,106,0) 75%);
  }
  .art--rose-side {
    left: 440px; top: 590px; width: 160px; height: 220px;
    background: radial-gradient(ellipse at 70% 40%, var(--rose-deep) 0%, var(--rose) 40%, rgba(240,185,188,0) 75%);
  }
  .title {
    position: absolute; font-family: "Pinyon Script", cursive;
    color: var(--ink); font-weight: 400; line-height: 1;
  }
  .title__line { position: absolute; white-space: nowrap; font-size: 124px; }
  .title__line--first { left: 105px; top: 320px; }
  .title__line--second { left: 68px; top: 455px; }
  .divider {
    position: absolute; left: 227px; top: 691px; width: 148px; height: 2px;
    background: var(--rule);
  }
  .tagline {
    position: absolute; left: 0; width: 600px; top: 742px; text-align: center;
    font-family: "Montserrat", sans-serif; font-weight: 600; font-size: 28px;
    letter-spacing: 0.36em; padding-left: 0.36em; color: var(--ink);
  }
  .seal { position: absolute; left: -4px; top: 742px; width: 116px; height: 116px; }
  .info {
    position: absolute; left: 0; top: 832px; width: 600px; height: 218px;
    background: var(--info-band);
  }
  .drink-name {
    position: absolute; left: 0; width: 600px; top: 18px; text-align: center;
    font-family: "Mrs Saint Delafield", cursive; font-size: 54px; color: var(--ink);
    padding-left: 60px;
  }
  .specs {
    position: absolute; left: 12px; right: 12px; top: 66px; height: 98px;
    border-top: 1.5px solid var(--rule); border-bottom: 1.5px solid var(--rule);
    display: flex; align-items: center;
    font-family: "Oswald", sans-serif; color: var(--ink);
  }
  .specs__cell {
    display: flex; align-items: center; justify-content: center; gap: 8px;
    height: 62px;
  }
  .specs__cell + .specs__cell { border-left: 2px solid var(--ink); }
  .specs__cell--abv { width: 210px; font-size: 30px; font-weight: 500; }
  .specs__cell--volume { width: 175px; font-size: 46px; font-weight: 600; }
  .specs__cell--batch { flex: 1; font-size: 30px; font-weight: 500; }
  .specs__dots { flex: 1; border-bottom: 2px dotted var(--ink); height: 0; margin-top: 16px; }
  .specs__unit { font-size: 0.7em; }
</style>
</head>
<body>
<main class="canvas">
  <section class="label">
    <div class="art art--rose-top" role="img" aria-label="Botanical illustration of two pink roses with green leaves"></div>
    <div class="art art--leaves" role="img" aria-label="Rose leaves trailing down the left edge"></div>
    <div class="art art--rose-side" role="img" aria-label="Botanical illustration of a pink rose with buds"></div>

    <h1 class="title">
      <span class="title__line title__line--first">Hollow</span>
      <span class="title__line title__line--second">lantern</span>
    </h1>

    <div class="divider"></div>
    <p class="tagline">SMALL BATCH</p>

    <svg class="seal" viewBox="0 0 116 116" aria-hidden="true">
      <circle cx="58" cy="58" r="54" fill="none" stroke="var(--gold)" stroke-width="2"/>
      <circle cx="58" cy="58" r="27" fill="none" stroke="var(--gold)" stroke-width="2"/>
    </svg>

    <div class="info">
      <p class="drink-name">My Drink Name</p>
      <div class="specs">
        <div class="specs__cell specs__cell--abv"><span class="specs__dots"></span><span>% ALC/VOL</span></div>
        <div class="specs__cell specs__cell--volume"><span>750<span class="specs__unit">ML</span></span></div>
        <div class="specs__cell specs__cell--batch"><span>BATCH NO</span><span class="specs__dots"></span></div>
      </div>
    </div>
  </section>
</main>
</body>
</html>
```